Business Card Design

sole trader electrician looking for an eye catching business card which includes the logo and all business details.

Industry/Entity Type

Electrician

Contact Information for Business Card

Peter Lowe Sparkworks , 0493157264, peterklowe27@voltmail.example, licence number 538207, Abn 41038275516, PLS is the logo of the company.

Font styles to use
Serif

```html
<!DOCTYPE html>
<html lang="en">
<head>
<meta charset="utf-8">
<title>Peter Lowe Sparkworks – Business Card</title>
<link href="https://fonts.googleapis.com/css2?family=Berkshire+Swash&family=Arimo:wght@400;700&display=swap" rel="stylesheet">
<style>
  :root {
    --card-bg: #ffffff;
    --ink: #111111;
    --brand-red: #d3172e;
    --brand-gold: #e2b437;
  }
  * { margin: 0; padding: 0; box-sizing: border-box; }
  html, body {
    width: 800px;
    height: 1200px;
    overflow: hidden;
    background: var(--card-bg);
  }
  .business-card {
    position: relative;
    width: 800px;
    height: 1200px;
    background: var(--card-bg);
    color: var(--ink);
    font-family: "Arimo", Arial, sans-serif;
    text-align: center;
  }
  .business-name {
    position: absolute;
    top: 90px;
    left: 0;
    right: 0;
    font-family: "Berkshire Swash", Georgia, serif;
    font-weight: 400;
    font-size: 72px;
    line-height: 100px;
    letter-spacing: 1px;
  }
  .brand-mark {
    position: absolute;
    top: 400px;
    left: 0;
    right: 0;
    display: flex;
    align-items: center;
    justify-content: center;
    gap: 28px;
  }
  .brand-mark__square {
    width: 90px;
    height: 90px;
    background: var(--brand-red);
  }
  .brand-mark__name {
    font-family: "Arimo", Arial, sans-serif;
    font-weight: 700;
    font-size: 150px;
    line-height: 1;
    color: var(--brand-red);
  }
  .contact {
    position: absolute;
    top: 810px;
    left: 0;
    right: 0;
  }
  .contact__phone {
    font-size: 50px;
    line-height: 70px;
  }
  .contact__phone strong { font-weight: 700; }
  .contact__email {
    font-size: 42px;
    font-weight: 700;
    line-height: 64px;
  }
  .credentials {
    position: absolute;
    bottom: 50px;
    left: 0;
    right: 0;
    font-size: 28px;
  }
</style>
</head>
<body>
  <main class="business-card">
    <h1 class="business-name">Peter Lowe<br>Sparkworks</h1>

    <div class="brand-mark">
      <span class="brand-mark__square" aria-hidden="true"></span>
      <span class="brand-mark__name">PLS</span>
    </div>

    <section class="contact">
      <p class="contact__phone">phone: <strong>0493-157-264</strong></p>
      <p class="contact__email">peterklowe27@voltmail.example</p>
    </section>

    <p class="credentials">Licence #538207 / Abn 41038275516</p>
  </main>
</body>
</html>
```